A Real Estate Company Needs a Business Card Design

We need a business card design for a new company based in Boston MA called "Brackenfield Real Estate LLC" we are a small company but we like a big corporate look, a simple, sleek, modern and progressive look. we would like the option of having a design that could include the real estate agents personal photo and also a design if the realtor decides not to have a photo. we do not have LOGO at this moment, please use any property look pic corporate with word" Brackenfield Real Estate LLC" please see attached file as an example.
Industry/Entity Type
Business

```html
<!DOCTYPE html>
<html lang="en">
<head>
<meta charset="UTF-8">
<title>Brackenfield Real Estate LLC – Business Card</title>
<link href="https://fonts.googleapis.com/css2?family=Rosarivo&display=swap" rel="stylesheet">
<style>
  :root {
    --backdrop: #161616;
    --card-dark: #38383a;
    --card-light: #ffffff;
    --ink-light: #f2f2f2;
    --ink-dark: #2e2e30;
    --ink-muted: #d6d6d6;
  }
  * { box-sizing: border-box; margin: 0; padding: 0; }
  html, body {
    width: 1200px;
    height: 800px;
    overflow: hidden;
    background: var(--backdrop);
    font-family: "Rosarivo", Georgia, serif;
  }
  .canvas {
    position: relative;
    width: 1200px;
    height: 800px;
    display: flex;
    flex-direction: column;
    align-items: center;
    justify-content: center;
    gap: 48px;
  }
  .card {
    position: relative;
    width: 560px;
    height: 320px;
    background: var(--card-dark);
    overflow: hidden;
    box-shadow: 0 10px 30px rgba(0,0,0,0.5);
  }

  /* Front */
  .card--front {
    display: flex;
    align-items: center;
    justify-content: center;
  }
  .brand {
    display: flex;
    align-items: center;
    gap: 14px;
  }
  .brand__mark {
    width: 18px;
    height: 18px;
    background: currentColor;
  }
  .brand__name {
    font-size: 30px;
    font-weight: 400;
    letter-spacing: 0.2px;
  }
  .card--front .brand { color: var(--ink-light); }

  /* Back */
  .card__band {
    position: absolute;
    left: 0; top: 0;
    width: 100%;
    height: 150px;
    background: var(--card-light);
    display: flex;
    align-items: center;
    justify-content: center;
  }
  .card__band .brand { color: var(--ink-dark); }
  .card__band .brand__name { font-size: 24px; }
  .card__band .brand__mark { width: 14px; height: 14px; }

  .contact {
    position: absolute;
    left: 0; top: 150px;
    width: 100%;
    height: 170px;
    display: flex;
    align-items: center;
    justify-content: center;
    gap: 26px;
    color: var(--ink-light);
  }
  .person { text-align: right; }
  .person__name { font-size: 34px; line-height: 1.1; }
  .person__role { font-size: 20px; color: var(--ink-muted); padding-right: 30px; }
  .divider {
    width: 2px;
    height: 100px;
    background: var(--ink-light);
  }
  .details {
    list-style: none;
    font-size: 14px;
    line-height: 1.7;
    color: var(--ink-muted);
    min-width: 150px;
  }
</style>
</head>
<body>
  <main class="canvas">
    <section class="card card--front" aria-label="Card front">
      <div class="brand">
        <span class="brand__mark" aria-hidden="true"></span>
        <span class="brand__name">Brackenfield Real Estate LLC</span>
      </div>
    </section>

    <section class="card card--back" aria-label="Card back">
      <div class="card__band">
        <div class="brand">
          <span class="brand__mark" aria-hidden="true"></span>
          <span class="brand__name">Brackenfield Real Estate LLC</span>
        </div>
      </div>
      <div class="contact">
        <div class="person">
          <p class="person__name">Your Name</p>
          <p class="person__role">Position</p>
        </div>
        <span class="divider" aria-hidden="true"></span>
        <ul class="details">
          <li>Phone:</li>
          <li>Email:</li>
          <li>Address:</li>
        </ul>
      </div>
    </section>
  </main>
</body>
</html>
```